Innovative Healthcare Technology Company needs a Business Card Design

We are in need of an innovative business card design for a new healthcare software company called "Lumenwise Data Partners". We develop software that creates medical assessment applications and mobile e-learning prevention services to reduce risk behaviors in adolescent and young adults. Our initial product, the "KESTREL App", conducts a tailored sexual risk assessment and provides a doctor with an insightful patient report to improve sexual risk counseling and ultimately reduce unintended pregnancy, STDs, etc.

We would like the design to incorporate our logo and branding colors (attached) in an innovative and creative manner. The final design should communicate professionalism and healthcare innovation. Our tag line is "prevention is the solution" (doesn't necessarily need to be included) and our target audience is doctors, medical directors, and medical business administrators. Please visit our website for additional info ourbrightmarq.com. Be creative and we look forward to seeing your designs!

Target Market(s)

healthcare - doctors, medical directors and medical business administrators

Industry/Entity Type

Healthcare

Contact Information for Business Card

We would like the design to incorporate our logo and branding colors (attached) in an innovative and creative manner. The final design should communicate professionalism and healthcare innovation. Our tag line is "prevention is the solution" (doesn't necessarily need to be included)

Font styles to use
Other font styles liked:
• quicksand

Requirements
Must have
• our logo and brand colors
• Name, (Mara Feldhovenik, PhD)
• Email (drmara@ourbrightmarq.com)
• phone (555.283.9170)
• Website (ourbrightmarq.com)
Should not have
• cartoon look

```html
<!DOCTYPE html>
<html lang="en">
<head>
<meta charset="utf-8">
<title>Lumenwise Data Partners – Business Card</title>
<link rel="stylesheet" href="https://fonts.googleapis.com/css2?family=Quicksand:wght@500&family=Open+Sans:wght@400;600;700&display=swap">
<style>
  :root {
    --page-bg: #1d1e21;
    --brand-blue: #1f5ba6;
    --brand-blue-light: #4586c4;
    --brand-blue-deep: #174a8c;
    --card-white: #ffffff;
    --ink-dark: #2a2a2a;
    --text-light: #ffffff;
  }
  * { margin: 0; padding: 0; box-sizing: border-box; }
  html, body {
    width: 1200px; height: 900px; overflow: hidden;
    background: var(--page-bg);
  }
  .canvas {
    position: relative; width: 1200px; height: 900px;
    display: flex; flex-direction: column; align-items: center; justify-content: center; gap: 40px;
  }
  .card {
    position: relative; width: 640px; height: 366px; overflow: hidden;
    box-shadow: 0 12px 30px rgba(0,0,0,0.55);
  }
  /* Front */
  .card--front {
    background: linear-gradient(100deg, var(--brand-blue-deep) 0%, var(--brand-blue) 45%, var(--brand-blue-light) 100%);
    display: flex; align-items: center; justify-content: center; gap: 22px;
  }
  .brand-mark {
    width: 34px; height: 34px; background: var(--text-light); border-radius: 3px; flex: none;
  }
  .brand-name {
    font-family: "Quicksand", sans-serif; font-weight: 500;
    font-size: 40px; line-height: 1.05; color: var(--text-light); letter-spacing: 0.5px;
  }
  /* Back */
  .card--back { background: var(--card-white); }
  .back-logo {
    position: absolute; left: 40px; top: 88px;
    display: flex; align-items: center; gap: 14px;
  }
  .back-logo .brand-mark { width: 24px; height: 24px; background: var(--brand-blue); }
  .back-logo .brand-name { font-size: 27px; color: var(--brand-blue); }
  .holder {
    position: absolute; left: 378px; top: 34px;
    font-family: "Open Sans", sans-serif;
  }
  .holder__name { font-weight: 700; font-size: 19px; color: var(--brand-blue); }
  .holder__title { font-weight: 600; font-size: 13px; color: var(--ink-dark); margin-left: 14px; }
  .wave-band { position: absolute; inset: 0; width: 640px; height: 366px; }
  .contact-list {
    position: absolute; left: 392px; top: 228px; list-style: none;
    font-family: "Open Sans", sans-serif; font-size: 15px; color: var(--text-light);
  }
  .contact-list li { display: flex; align-items: center; gap: 12px; height: 27px; }
  .contact-list svg { width: 14px; height: 14px; flex: none; }
</style>
</head>
<body>
<main class="canvas">
  <section class="card card--front" aria-label="Card front">
    <span class="brand-mark"></span>
    <span class="brand-name">Lumenwise Data Partners</span>
  </section>

  <section class="card card--back" aria-label="Card back">
    <svg class="wave-band" viewBox="0 0 640 366" role="img" aria-label="Decorative blue wave band across the lower right of the card">
      <defs>
        <linearGradient id="bandFill" x1="0" y1="1" x2="1" y2="0">
          <stop offset="0" stop-color="#1b55a0"/>
          <stop offset="1" stop-color="#4586c4"/>
        </linearGradient>
      </defs>
      <path d="M0 325 C 200 320, 330 250, 420 180 C 490 130, 560 115, 640 112 L640 366 L0 366 Z" fill="url(#bandFill)"/>
    </svg>

    <div class="back-logo">
      <span class="brand-mark"></span>
      <span class="brand-name">Lumenwise Data Partners</span>
    </div>

    <div class="holder">
      <div class="holder__name">Mara Feldhovenik</div>
      <div class="holder__title">PHD</div>
    </div>

    <ul class="contact-list">
      <li>
        <svg viewBox="0 0 24 24" aria-hidden="true"><path fill="#fff" d="M6.6 10.8a15.1 15.1 0 0 0 6.6 6.6l2.2-2.2c.3-.3.7-.4 1-.2 1.1.4 2.3.6 3.6.6.6 0 1 .4 1 1V20c0 .6-.4 1-1 1A17 17 0 0 1 3 4c0-.6.4-1 1-1h3.5c.6 0 1 .4 1 1 0 1.3.2 2.5.6 3.6.1.3 0 .7-.2 1z"/></svg>
        555.283.9170
      </li>
      <li>
        <svg viewBox="0 0 24 24" aria-hidden="true"><g fill="none" stroke="#fff" stroke-width="2"><circle cx="12" cy="12" r="9"/><path d="M3 12h18M12 3c3 3 3 15 0 18M12 3c-3 3-3 15 0 18"/></g></svg>
        ourbrightmarq.com
      </li>
      <li>
        <svg viewBox="0 0 24 24" aria-hidden="true"><text x="12" y="18" text-anchor="middle" font-family="Open Sans, sans-serif" font-weight="700" font-size="20" fill="#fff">@</text></svg>
        drmara@ourbrightmarq.com
      </li>
    </ul>
  </section>
</main>
</body>
</html>
```